Cause bitches need love too!

I am creating an ad campaign. It will be a series of featured dogs in our shelter and they will contain a picture of the dog wich should be big enough to see on a yard sign and will change every week. I am placing the signs so that they lead you to the shelter. This is why I am also including the copy that says "you're almost there".

I have 4 tag lines:

1. Find unconditional Love.
2. She'll Love you furever!
3. He'll always listen.
4. Meet your new BFF

You're almost there 217 W Marlowe Ave
Open 10 - 7/Tues-Sat

The dimensions for the sign are 24" wide and 18" high

Every week we will have a different picture of a different dog (hopefully last week's dog gets adopted). Anyhow, I am printing out yard signs, meaning that instead of printing 160 different signs it would be ideal just to replace the photo. So far the copy that is permanent is: "You're almost there. 217 W. Marlowe Ave."

I could silhouette the image of the dog as well and super impose it on the sign, that's also a consideration, but ideally if I could have 4 tag lines I could print 40 signs of each and just replace the photo manually each week from my printer that would save costs.
Updates

Not enough designs to chose from and I edited the brief and committed to pay no matter what to increase the amount of designs as per your suggestions.

Target Market(s)

Animal lovers

Industry/Entity Type

Campaign

Font styles to use
Sans Serif

Colors

Designer to choose colors to be used in the design.

Requirements
Must have
• The dimensions for the sign are 24" wide and 18" high
Nice to have
• I want the signs to be hip, they should have a positive feel to them. You can alter the photos if you like. I am even open to new copy if you think something else works better.

```html
<!DOCTYPE html>
<html lang="en">
<head>
<meta charset="utf-8">
<title>Shelter Yard Sign – She'll Love you furever!</title>
<link rel="stylesheet" href="https://fonts.googleapis.com/css2?family=Kurale&family=Open+Sans:wght@400;600;700&display=swap">
<style>
  :root {
    --paper: #f4f5f6;
    --sage: #8aa99a;
    --sage-light: #a9c4b7;
    --headline: #7a665a;
    --ink: #4a4a4c;
    --ink-strong: #3c3c3e;
    --divider: #8fb0a1;
    --photo-light: #cfcbc8;
    --photo-mid: #b59a74;
    --photo-dark: #8c6a3e;
  }
  * { margin: 0; padding: 0; box-sizing: border-box; }
  html, body {
    width: 1200px;
    height: 900px;
    overflow: hidden;
    background: var(--paper);
  }
  .yard-sign {
    position: relative;
    width: 1200px;
    height: 900px;
    background: var(--paper);
    overflow: hidden;
  }
  .sign-shapes {
    position: absolute;
    inset: 0;
  }
  .tagline {
    position: absolute;
    left: 49px;
    top: 72px;
    font-family: "Kurale", Georgia, serif;
    font-weight: 400;
    font-size: 70px;
    line-height: 98px;
    color: var(--headline);
  }
  .tagline-rule {
    position: absolute;
    left: 47px;
    top: 379px;
    width: 360px;
    height: 2px;
    background: var(--divider);
  }
  .directions {
    position: absolute;
    left: 49px;
    top: 478px;
    font-family: "Open Sans", Arial, sans-serif;
    font-size: 32px;
    font-weight: 400;
    letter-spacing: 0.5px;
    color: var(--ink);
  }
  .address {
    position: absolute;
    left: 49px;
    top: 552px;
    display: flex;
    align-items: center;
    gap: 22px;
    font-family: "Open Sans", Arial, sans-serif;
    font-size: 33px;
    font-weight: 600;
    color: var(--ink-strong);
  }
  .address-pin { width: 24px; height: 36px; }
  .hours {
    position: absolute;
    left: 49px;
    top: 797px;
    font-family: "Open Sans", Arial, sans-serif;
    font-size: 33px;
    font-weight: 400;
    color: #ffffff;
  }
</style>
</head>
<body>
<main class="yard-sign">
  <svg class="sign-shapes" width="1200" height="900" viewBox="0 0 1200 900" aria-hidden="false">
    <defs>
      <linearGradient id="photoTones" x1="0" y1="0" x2="1" y2="1">
        <stop offset="0" stop-color="var(--photo-light)"/>
        <stop offset="0.45" stop-color="var(--photo-mid)"/>
        <stop offset="1" stop-color="var(--photo-dark)"/>
      </linearGradient>
    </defs>

    <!-- footer band -->
    <path class="footer-line" d="M0 697 Q 330 640 750 735" fill="none" stroke="#dcdfe0" stroke-width="3"/>
    <path class="footer-band" d="M0 711 Q 330 660 760 745 L 760 900 L 0 900 Z" fill="var(--sage)"/>

    <!-- faint paw area -->
    <rect class="paw-mark" role="img" aria-label="Faint paw print decoration" x="41" y="615" width="154" height="154" rx="60" fill="#c9d3cf" opacity="0.35"/>

    <!-- photo frame curves -->
    <path class="frame-sage" d="M756 0 Q 393 444 606 900 L 1200 900 L 1200 0 Z" fill="var(--sage-light)"/>
    <path class="frame-white" d="M792 0 Q 425 444 638 900 L 1200 900 L 1200 0 Z" fill="#ffffff"/>
    <path class="dog-photo" role="img" aria-label="Photo of the featured shelter dog of the week, a tan and black shepherd mix looking toward the viewer"
          d="M809 0 Q 448 442 655 900 L 1200 900 L 1200 0 Z" fill="url(#photoTones)"/>
  </svg>

  <h1 class="tagline">She'll<br>Love you<br>furever!</h1>
  <div class="tagline-rule"></div>

  <p class="directions">YOU'RE ALMOST THERE</p>
  <p class="address">
    <svg class="address-pin" viewBox="0 0 24 36" aria-hidden="true">
      <path d="M12 0C5.4 0 0 5.2 0 11.7 0 20.5 12 36 12 36s12-15.5 12-24.3C24 5.2 18.6 0 12 0zm0 16.5a5 5 0 1 1 0-10 5 5 0 0 1 0 10z" fill="var(--ink)"/>
    </svg>
    217 W Marlowe Ave
  </p>

  <p class="hours">Open 10 - 7/Tues-Sat</p>
</main>
</body>
</html>
```